Harbor Sushi & Steak Dinner Menu

I'm looking for a MENU design with a particular feel. I want to have a base template made that I can then use for future alterations to the menu; ie I can go in and change out different entrees as the menu changes but the template will remain the same. (Ideally it would be in an Apple Pages format.). Also ideally - dinner menu will occupy 2 pages 8.5 x 11. The restaurant's name is Harbor. It is a MODERN steak house that will also feature Sushi, a Raw Bar, Exquisite Cocktails and a sophisticated nightlife crowd. I have attached our LOGO, a secondary logo that we will be featuring throughout the project including on the menu cover (the gold U). Finally - I have attached the content that we would like to see. AGAIN - I REITERATE: High end dining and lounge atmosphere. A couple of restaurants / menus that I love are Morvendel in NYC and Pellucid Steakhouse in Long Island NY. Please do not duplicate - just trying to offer some suggestions.

Requirements
Must have
• A sophisticated and elegant feel without being stuffy or old.

```html
<!DOCTYPE html>
<html lang="en">
<head>
<meta charset="utf-8">
<title>Harbor Sushi &amp; Steak — Dinner Menu</title>
<link rel="stylesheet" href="https://fonts.googleapis.com/css2?family=Montserrat:wght@400;500;600;700&family=Poppins:wght@400&display=swap">
<style>
:root{
  --backdrop:#e9e9e9;
  --page:#151415;
  --page-hi:#1d1c1d;
  --red:#e5264a;
  --gold:#dcc073;
  --text:#ececec;
  --bullet:#9a9a9a;
  --rule:#b81f3c;
  --divider:#555;
}
*{box-sizing:border-box;margin:0;padding:0}
html,body{width:1200px;height:783px;overflow:hidden;background:var(--backdrop)}
body{position:relative;font-family:"Montserrat",sans-serif;color:var(--text)}
.page{position:absolute;top:67px;width:517px;height:670px;
  background:linear-gradient(135deg,var(--page-hi),var(--page) 40%,var(--page-hi) 70%,var(--page));
  box-shadow:0 6px 14px rgba(0,0,0,.25)}
.page--front{left:50px}
.page--back{left:623px}
.col{position:absolute}
.divider{position:absolute;width:1px;background:var(--divider)}
.section{margin-bottom:14px}
.section h2{display:flex;align-items:center;gap:8px;font-weight:700;font-size:11.2px;color:var(--red);letter-spacing:.2px;margin-bottom:4px;white-space:nowrap}
.section h2::after{content:"";flex:1;height:1px;background:var(--rule);margin-top:3px}
.section ul{list-style:none}
.section li{position:relative;padding-left:13px;font-size:7.9px;line-height:10.2px;margin-bottom:1.7px}
.section li::before{content:"";position:absolute;left:2px;top:4px;width:2.6px;height:2.6px;border-radius:50%;background:var(--bullet)}
.name{color:var(--gold)}
.gold li{color:var(--gold)}
.two-col{display:grid;grid-template-columns:1fr 1fr;column-gap:10px}
.two-col li.plain::before{display:none}
.emph{color:var(--gold);font-weight:600;font-size:9.5px}
.brand{position:absolute;left:0;right:0;display:flex;justify-content:center;align-items:center;gap:10px}
.brand-name{font-weight:500;font-size:36px;letter-spacing:9px;color:var(--gold)}
.brand-dot{width:12px;height:12px;border-radius:50%;background:var(--red)}
.ribbon{position:absolute;left:453px;top:0;width:46px;height:78px}
.footer{position:absolute;left:14px;right:14px;top:640px;border-top:1px solid var(--rule);
  padding-top:8px;text-align:center;font-family:"Poppins",sans-serif;font-size:8px;letter-spacing:1px;color:var(--text);word-spacing:2px}
.footer .sep{margin:0 14px}
</style>
</head>
<body>

<section class="page page--front" aria-label="Menu front">
  <div class="brand" style="top:48px"><span class="brand-dot"></span><span class="brand-name">HARBOR</span></div>

  <div class="col" style="left:24px;top:146px;width:203px">
    <div class="section">
      <h2>SUSHI / SASHIMI</h2>
      <ul>
        <li><span class="name">Toro;</span> blue fin tuna belly (gf)</li>
        <li><span class="name">Ebi;</span> cooked shrimp (gf)</li>
        <li><span class="name">Hamachi;</span> yellowtail (gf)</li>
        <li><span class="name">Uni;</span> sea urchin (gf)</li>
        <li><span class="name">Hirame;</span> fluke (gf)</li>
        <li><span class="name">Unagi;</span> fresh water eel (gf)</li>
        <li><span class="name">Sake;</span> salmon (gf)</li>
        <li><span class="name">Madai;</span> red snapper (gf)</li>
        <li><span class="name">Maguro;</span> tuna (gf)</li>
      </ul>
    </div>
    <div class="section">
      <h2>CLASSIC ROLLS</h2>
      <ul>
        <li><span class="name">Yellowtail;</span> inside out roll with scallions (gf)</li>
        <li><span class="name">Spicy Tuna or Salmon or Yellowtail;</span> spicy mayo</li>
        <li><span class="name">California:</span> crab meat, cucumber and avocado (gf)</li>
        <li><span class="name">Vegetable:</span> avocado, cucumber, asparagus and pickled reddish (gf)</li>
        <li><span class="name">Spider:</span> soft shell crab and avocado with eel sauce</li>
        <li><span class="name">Shrimp Tempura:</span> deep fried tempura shrimp and eel sauce</li>
        <li><span class="name">Alaskan;</span> salmon and avocado (gf)</li>
      </ul>
    </div>
    <div class="section">
      <h2>SPECIAL ROLLS</h2>
      <ul>
        <li><span class="name">The Harbor:</span> tuna, salmon, yellowtail, avocado, spicy mayo, soy bean paper</li>
        <li><span class="name">King Crab Rainbow:</span> king crab, avocado, cucumbers, assorted fish on top</li>
        <li><span class="name">Empress:</span> Shrimp tempura, spicy tuna on top, eel sauce, spicy mayo</li>
        <li><span class="name">Spicy Girl:</span> Spicy crunchy crab meat, cucumber, shrimp on top</li>
        <li><span class="name">Dragon:</span> Eel, cucumber, avocado, and tobiko on top, eel sauce</li>
        <li><span class="name">Yummy:</span> spicy crunchy salmon, avocado, mango and salmon on top</li>
        <li><span class="name">No. 9:</span> Shrimp Tempura, avocado, kani, spicy mayo, tobiko</li>
        <li><span class="name">Sunrise Roll:</span> spicy crunchy tuna and avocado, spicy crunchy salmon on top</li>
      </ul>
    </div>
  </div>

  <div class="divider" style="left:246px;top:150px;height:472px"></div>

  <div class="col" style="left:268px;top:150px;width:221px">
    <div class="section" style="margin-bottom:18px">
      <h2>SUSHI PLATTERS</h2>
      <ul>
        <li><span class="name">Small:</span> Five Pieces assorted sushi, nine pieces sashimi, spicy tuna roll (gf)</li>
        <li><span class="name">Large:</span> Eight Pieces assorted sushi, eighteen pieces of sashimi, alaskan roll, rainbow roll (gf)</li>
      </ul>
    </div>
    <div class="section" style="margin-bottom:18px">
      <h2>SEAFOOD RAW BAR</h2>
      <ul class="two-col">
        <li>Lobster Cocktail</li><li class="plain">Oysters on the Half Shell</li>
        <li>Shrimp Cocktail</li><li class="plain">Colossal Crab Cocktail</li>
        <li>Clams on the Half Shell</li>
      </ul>
    </div>
    <div class="section" style="margin-bottom:18px">
      <h2>RAW BAR PLATE FOR ONE</h2>
      <ul>
        <li>Two Shrimp, Half of a One Pound Lobster,</li>
        <li>Two Clams, One East Coast Oyster, One West Coast Oyster</li>
      </ul>
    </div>
    <div class="section" style="margin-bottom:20px">
      <h2>SEAFOOD PLATTERS (GF)</h2>
      <ul>
        <li>Shrimp, Oysters, Clams, Lobster and Crab</li>
        <li class="emph">Large or Colossal</li>
      </ul>
    </div>
    <div class="section">
      <h2>APPS</h2>
      <ul>
        <li><span class="name">BAO Bun;</span> hoisin bbq pancetta cut pork loin, crispy onions, micro mint</li>
        <li><span class="name">Five Spice Crispy Popcorn Crusted Prawns (2);</span> classic burre blanc</li>
        <li><span class="name">Jumbo Lump Crab;</span> citrus miso drizzle, spring pea puree, micro greens</li>
        <li><span class="name">Crispy Wonton Napoleon;</span> cucumber gallete, ahi tuna, jumbo lump crab meat, wasabi aioli, shoestring wontons</li>
        <li><span class="name">PEI Mussels;</span> charred artichoke hearts, blistered heirloom tomatoes, garlic white wine broth</li>
        <li><span class="name">New Zealand or Domestic Small Eye Lamb Chop (1);</span> crispy porcini risotto cake</li>
      </ul>
    </div>
  </div>

  <footer class="footer">Call : 0198 765 432<span class="sep">|</span>Mail : info@harbordining.com<span class="sep">|</span>Visit Us : www.harbordining.com</footer>
</section>

<section class="page page--back" aria-label="Menu back">
  <svg class="ribbon" viewBox="0 0 46 78" aria-hidden="true">
    <defs><linearGradient id="ribbonFill" x1="0" y1="0" x2="0" y2="1"><stop offset="0" stop-color="#e9d69a"/><stop offset="1" stop-color="#c98a5e"/></linearGradient></defs>
    <path d="M0 0H46V78L23 68L0 78Z" fill="url(#ribbonFill)"/>
  </svg>

  <div class="col" style="left:24px;top:30px;width:202px">
    <div class="section" style="margin-bottom:16px">
      <h2>SALADS</h2>
      <ul>
        <li><span class="name">Classic Wedge;</span> bleu cheese, bacon lardons, heirloom tomatoes</li>
        <li><span class="name">Mixed Baby Greens;</span> heirloom tomatoes, cucumber, red onion, dijon vinaigrette</li>
        <li><span class="name">Tabulleh;</span> buckwheat grain, fresh mint, tomato concasse, cucumber, parsley, fresh squeezed lemon, EVOO., salt and pepper</li>
        <li><span class="name">Tomato Mozzarella Salad / Burratta</span></li>
        <li><span class="name">Spinach Salad;</span> green apple, feta, currants, with per-simmons vinaigrette</li>
        <li><span class="name">Kale Caesar;</span> homemade cacio e'peppe dressing, pecorino and parmesan cheese, toasted croutons.</li>
      </ul>
    </div>
    <div class="section">
      <h2>ENTREES</h2>
      <ul>
        <li><span class="name">Pan Roasted Miso Glazed Black Cod;</span> green tea noodle stir fry; Napa cabbage,</li>
        <li><span class="name">Pan Seared Striped Bass;</span> lobster succotash in a tomato saffron brothcarrot, Japanese eggplant</li>
        <li><span class="name">E.V.O.O. Salted / Grilled Swordfish;</span> sun dried tomato, olive and caper tapenade, over basmati rice</li>
        <li><span class="name">Grilled Half Chicken;</span> sun dried tomato and basil Israeli cous-cous, pan au jus</li>
        <li><span class="name">Roasted Fresh Caviatelle Ratatoille;</span> vegetable broth</li>
        <li><span class="name">Lobster Cartoccio;</span> shrimp, mussels, clams, fresh herb tomato broth, tossed with bucatini Charred Artichoke Hearts, heirloom tomatoes, caper berries, spring onions, fresh basil, white wine reduction over forbidden rice (gf)</li>
        <li><span class="name">Mediterranean Grilled Veggie Plate;</span> artichoke hearts, Japanese eggplant, green &amp; white asparagus, seared heirloom tomatoes, roasted baby carrots, cauliflower rice, evoo &amp; fig drizzle (gf)</li>
      </ul>
    </div>
  </div>

  <div class="divider" style="left:261px;top:30px;height:476px"></div>

  <div class="col" style="left:279px;top:30px;width:202px">
    <div class="section gold" style="margin-bottom:22px">
      <h2 style="margin-right:28px">USDA PRIME STEAKS (gf)</h2>
      <ul>
        <li>10 Oz Filet</li>
        <li>14 or 16 oz New York Strip</li>
        <li>24 oz Boneless Ribeye</li>
        <li>36 oz Bone in Rib Eye</li>
        <li>Berkshire Pork Chop</li>
        <li>SAUCES</li>
      </ul>
    </div>
    <div class="section gold" style="margin-bottom:22px">
      <h2>SAUCES</h2>
      <ul>
        <li>Cabernet Demi Glaz</li>
        <li>Gorganzola Brulle Cream</li>
        <li>Truffled Wild Mushroom Ragu</li>
        <li>Horseradish Cream</li>
        <li>House Steak Sauce</li>
      </ul>
    </div>
    <div class="section gold" style="margin-bottom:14px">
      <h2>SAUCES</h2>
      <ul>
        <li style="margin-bottom:3.8px">Mashed Idaho Potatoes</li>
        <li style="margin-bottom:3.8px">Bacon, Sweet Corn, Caramelized Vidalia Onion fingerling potatoes</li>
        <li style="margin-bottom:3.8px">Roasted Peanut Potatoes</li>
        <li style="margin-bottom:3.8px">Creamed Spinach</li>
        <li style="margin-bottom:3.8px">Sautéed Spinach</li>
        <li style="margin-bottom:3.8px">Grilled Asparagus</li>
        <li style="margin-bottom:3.8px">French Beans</li>
        <li style="margin-bottom:3.8px">Israeli Cous Cous</li>
        <li style="margin-bottom:3.8px">Sweet Potato Steak Fries</li>
        <li style="margin-bottom:3.8px">Corn Skillet</li>
      </ul>
    </div>
    <div class="section gold">
      <h2>DESSERTS</h2>
      <ul><li>T.B.D. - separate menu</li></ul>
    </div>
  </div>

  <div class="brand" style="top:540px;left:10px;right:auto;width:502px"><span class="brand-dot"></span><span class="brand-name">HARBOR</span></div>

  <footer class="footer">Call : 0198 765 432<span class="sep">|</span>Mail : info@harbordining.com<span class="sep">|</span>Visit Us : www.harbordining.com</footer>
</section>

</body>
</html>
```